Business Card for Willowcrest Terrain Advisors

We need a business card for Willowcrest Terrain Advisors. The company website address is provided below. The company logo is attached. We provide specialized permafrost services to the mining, transportation, and oil & gas industries. The card should be prepared for:
Dominic Halloway, PhD.
Willowcrest Terrain Advisors
PO Box 418529
Birch Hollow, Alaska 99612
Direct: +1-907-555-2964
Email: dhalloway@terrainadvisors-example.com
Website: www.willowcrestterrainadvisors-example.com

```html
<!DOCTYPE html>
<html lang="en">
<head>
<meta charset="utf-8">
<title>Willowcrest Terrain Advisors – Business Card</title>
<link href="https://fonts.googleapis.com/css2?family=Arimo:wght@400;700&display=swap" rel="stylesheet">
<style>
  :root {
    --backdrop: #d9dadc;
    --paper: #ffffff;
    --navy: #111b24;
    --rule: #7d8187;
    --ink-light: #ffffff;
    --ink-soft: #d4d8dc;
    --brand-dark: #131d26;
    --brand-silver: #8c939b;
  }
  * { box-sizing: border-box; margin: 0; padding: 0; }
  html, body { width: 1200px; height: 800px; overflow: hidden; }
  body {
    background: var(--backdrop);
    font-family: "Arimo", Arial, sans-serif;
    display: flex;
    align-items: center;
    justify-content: center;
    gap: 40px;
  }
  .card {
    width: 540px;
    height: 308px;
    border-radius: 18px;
    overflow: hidden;
    position: relative;
    box-shadow: 0 6px 18px rgba(0,0,0,0.18);
  }

  /* Front */
  .card--front { background: var(--navy); display: flex; flex-direction: column; }
  .front__brand {
    background: var(--paper);
    height: 132px;
    display: flex;
    flex-direction: column;
    justify-content: center;
    padding-left: 44px;
    border-bottom: 4px solid var(--rule);
  }
  .brand {
    font-weight: 700;
    text-transform: uppercase;
    line-height: 1;
  }
  .brand__main { font-size: 40px; letter-spacing: 2px; display: block; }
  .brand__sub { font-size: 13px; letter-spacing: 6.2px; display: block; margin-top: 8px; }
  .front__brand .brand { color: var(--brand-dark); }

  .front__details {
    flex: 1;
    display: flex;
    padding: 30px 28px 0 30px;
    color: var(--ink-light);
  }
  .person { width: 306px; padding-right: 20px; }
  .person__name { font-weight: 700; font-size: 20px; }
  .person__title { font-size: 12px; text-align: right; color: var(--ink-soft); margin-top: 3px; }
  .person__links { margin-top: 18px; list-style: none; }
  .person__links li {
    font-size: 11.5px;
    color: var(--ink-soft);
    display: flex;
    align-items: center;
    justify-content: flex-end;
    gap: 6px;
    margin-bottom: 5px;
    white-space: nowrap;
  }
  .divider { width: 1px; background: var(--rule); margin: 4px 0 40px; }
  .office { padding-left: 18px; list-style: none; }
  .office li { font-size: 12.5px; color: var(--ink-soft); margin-bottom: 6px; display: flex; align-items: center; gap: 6px; }
  .icon { width: 11px; height: 11px; flex: none; fill: var(--ink-soft); }

  /* Back */
  .card--back {
    background: var(--navy);
    display: flex;
    align-items: center;
    justify-content: center;
  }
  .card--back .brand { color: var(--brand-silver); text-align: center; }
  .card--back .brand__main { font-size: 46px; }
  .card--back .brand__sub { font-size: 15px; letter-spacing: 7.4px; margin-top: 10px; }
</style>
</head>
<body>

  <section class="card card--front" aria-label="Card front">
    <header class="front__brand">
      <div class="brand">
        <span class="brand__main">Willowcrest</span>
        <span class="brand__sub">Terrain Advisors</span>
      </div>
    </header>
    <div class="front__details">
      <div class="person">
        <p class="person__name">Dominic Halloway, PhD.</p>
        <p class="person__title">President</p>
        <ul class="person__links">
          <li>dhalloway@terrainadvisors-example.com
            <svg class="icon" viewBox="0 0 12 12"><path d="M0 2h12v8H0z M1 3v.4l5 3.2 5-3.2V3z" fill-rule="evenodd"/></svg>
          </li>
          <li>www.willowcrestterrainadvisors-example.com
            <svg class="icon" viewBox="0 0 12 12"><circle cx="6" cy="6" r="5.5"/><path d="M1 6h10M6 .5c-2.2 2.5-2.2 8.5 0 11M6 .5c2.2 2.5 2.2 8.5 0 11" stroke="#111b24" stroke-width="0.9" fill="none"/></svg>
          </li>
        </ul>
      </div>
      <div class="divider"></div>
      <ul class="office">
        <li>
          <svg class="icon" viewBox="0 0 12 12"><path d="M2.4 0.6l2 2.2-1 1.3c.7 1.6 2 2.9 3.5 3.6l1.3-1 2.2 2-1.2 2.2C5 10.6 1.4 7 .4 1.8z"/></svg>
          +1-907-555-2964
        </li>
        <li>PO Box 418529</li>
        <li>Birch Hollow, Alaska 99612</li>
      </ul>
    </div>
  </section>

  <section class="card card--back" aria-label="Card back">
    <div class="brand">
      <span class="brand__main">Willowcrest</span>
      <span class="brand__sub">Terrain Advisors</span>
    </div>
  </section>

</body>
</html>
```